PLOVEN Business Card

Coastal Build Additions and Refits. I need a business card designed for this new high end renovation business. I would like the logo centered on the back side with the ABN (37 915 402 176) on the bottom right hand corner.

I would like the following information placed on the other side along with some customized pattern or design.

Derek Collwood
Director
Phone: 1300 480 957
Fax: (02) 8145 9021
Website: www.plovenbuilders.com.au
Email: d.collwood@plovenbuilders.com.au
PO Box 87,
Kelvinbrook NSW 2069

(FB Logo) PLOVEN - Coastal Build Additions and Refits

The final design should communicate professionalism and trust.

Back side background colour: white
Front side: Undecided

```html
<!DOCTYPE html>
<html lang="en">
<head>
<meta charset="utf-8">
<title>PLOVEN Business Card</title>
<link rel="stylesheet" href="https://fonts.googleapis.com/css2?family=Maven+Pro:wght@400;500;700&display=swap">
<style>
  :root {
    --stage: #3e3e40;
    --card-white: #ffffff;
    --card-grey: #e2e2e4;
    --brand-blue: #1d4f86;
    --band-light: #5a5a5c;
    --band-dark: #2e2e30;
    --swoosh: #3a3a3c;
    --text-light: #ffffff;
    --text-muted: #5a5a5c;
    --rule: #d8d8d8;
  }
  * { margin: 0; padding: 0; box-sizing: border-box; }
  html, body { width: 1200px; height: 999px; overflow: hidden; }
  body {
    background: var(--stage);
    font-family: "Maven Pro", sans-serif;
    position: relative;
  }
  .card {
    position: absolute;
    width: 763px;
    height: 435px;
    overflow: hidden;
    box-shadow: 0 6px 18px rgba(0,0,0,0.35);
  }
  .card--front { left: 82px; top: 62px; background: var(--card-white); }
  .card--back {
    left: 356px; top: 530px;
    background: radial-gradient(ellipse at 55% 50%, var(--card-white) 0%, var(--card-white) 35%, var(--card-grey) 100%);
  }
  .brand {
    position: absolute;
    left: 0; right: 0;
    text-align: center;
    color: var(--brand-blue);
  }
  .brand__name { font-weight: 700; letter-spacing: 4px; line-height: 1; }
  .brand__tagline { font-weight: 700; text-transform: uppercase; letter-spacing: 1px; }
  .card--front .brand { top: 58px; }
  .card--front .brand__name { font-size: 44px; }
  .card--front .brand__tagline { font-size: 12px; margin-top: 8px; }
  .card--back .brand { top: 160px; }
  .card--back .brand__name { font-size: 62px; }
  .card--back .brand__tagline { font-size: 16px; margin-top: 12px; }
  .abn {
    position: absolute;
    right: 28px; bottom: 22px;
    font-size: 14px;
    font-weight: 500;
    color: var(--text-muted);
    letter-spacing: 0.5px;
  }
  .person {
    position: absolute;
    top: 168px; left: 0; right: 0;
    text-align: center;
    color: var(--brand-blue);
  }
  .person__name { font-size: 30px; font-weight: 700; line-height: 1.1; }
  .person__role { font-size: 21px; font-weight: 500; }
  .band { position: absolute; left: 0; top: 0; }
  .contact {
    position: absolute;
    color: var(--text-light);
    font-size: 19px;
    line-height: 1.25;
    list-style: none;
  }
  .contact li { display: flex; align-items: flex-start; }
  .contact svg { flex: none; margin-right: 18px; margin-top: 2px; }
  .contact--left { left: 52px; top: 318px; }
  .contact--left li + li { margin-top: 14px; }
  .contact--right { left: 370px; top: 310px; }
  .contact--right li + li { margin-top: 11px; }
  .contact--right svg { margin-right: 14px; }
  .divider {
    position: absolute;
    left: 357px; top: 300px;
    width: 2px; height: 110px;
    background: var(--rule);
  }
</style>
</head>
<body>

<section class="card card--front" aria-label="Card front">
  <svg class="band" width="763" height="435" viewBox="0 0 763 435">
    <defs>
      <radialGradient id="bandShade" cx="0.3" cy="0.55" r="0.8">
        <stop offset="0" stop-color="var(--band-light)"/>
        <stop offset="1" stop-color="var(--band-dark)"/>
      </radialGradient>
    </defs>
    <path d="M0 306 Q380 262 763 308 L763 435 L0 435 Z" fill="url(#bandShade)"/>
    <path d="M305 288 Q560 262 763 300 L763 306 Q560 274 305 288 Z" fill="var(--swoosh)"/>
  </svg>

  <div class="brand">
    <div class="brand__name">PLOVEN</div>
    <div class="brand__tagline">Coastal Build Additions &amp; Refits</div>
  </div>

  <div class="person">
    <div class="person__name">Derek Collwood</div>
    <div class="person__role">Director</div>
  </div>

  <ul class="contact contact--left">
    <li>
      <svg width="20" height="28" viewBox="0 0 20 28" aria-hidden="true"><path d="M10 1a8.5 8.5 0 0 0-8.5 8.5C1.5 16 10 27 10 27s8.5-11 8.5-17.5A8.5 8.5 0 0 0 10 1zm0 12a3.5 3.5 0 1 1 0-7 3.5 3.5 0 0 1 0 7z" fill="#fff"/></svg>
      <span>PO Box 87,<br>Kelvinbrook NSW 2069</span>
    </li>
    <li>
      <svg width="20" height="20" viewBox="0 0 24 24" aria-hidden="true"><path d="M6.6 10.8a15.1 15.1 0 0 0 6.6 6.6l2.2-2.2a1 1 0 0 1 1-.25 11.4 11.4 0 0 0 3.6.57 1 1 0 0 1 1 1V20a1 1 0 0 1-1 1A17 17 0 0 1 3 4a1 1 0 0 1 1-1h3.5a1 1 0 0 1 1 1c0 1.25.2 2.450.57 3.57a1 1 0 0 1-.25 1z" fill="#fff"/></svg>
      <span>1300 480 957</span>
    </li>
  </ul>

  <div class="divider"></div>

  <ul class="contact contact--right">
    <li>
      <svg width="20" height="20" viewBox="0 0 20 20" aria-hidden="true"><rect x="5" y="1" width="10" height="7" fill="#fff"/><rect x="1" y="9" width="18" height="10" rx="1" fill="#fff"/><rect x="4" y="12" width="12" height="2" fill="#3a3a3c"/></svg>
      <span>(02) 8145 9021</span>
    </li>
    <li>
      <svg width="20" height="20" viewBox="0 0 20 20" aria-hidden="true"><circle cx="10" cy="10" r="8.5" fill="none" stroke="#fff" stroke-width="1.8"/><ellipse cx="10" cy="10" rx="3.6" ry="8.5" fill="none" stroke="#fff" stroke-width="1.5"/><path d="M1.5 10h17M3 5.5h14M3 14.5h14" stroke="#fff" stroke-width="1.4"/></svg>
      <span>www.plovenbuilders.com.au</span>
    </li>
    <li>
      <svg width="20" height="20" viewBox="0 0 20 20" aria-hidden="true"><path d="M2 8l8-6 8 6v10H2z" fill="#fff"/><path d="M2 8l8 6 8-6" fill="none" stroke="#3a3a3c" stroke-width="1.4"/></svg>
      <span>d.collwood@plovenbuilders.com.au</span>
    </li>
  </ul>
</section>

<section class="card card--back" aria-label="Card back">
  <div class="brand">
    <div class="brand__name">PLOVEN</div>
    <div class="brand__tagline">Coastal Build Additions &amp; Refits</div>
  </div>
  <div class="abn">ABN 37 915 402 176</div>
</section>

</body>
</html>
```